Large Format Graphics for Printed Vinyl Window Covering

The Graphics will be printed to fit windows 60inch wide by 53inch tall should contain a variety of images showing the products attached and tagline text area. Logo will be on graphics but should not take away from the focus of the products.
Deliverables are three different graphics to cover separate windows and be in full scale to sizes mentioned above with files in AI, PSD and PDF.

Font styles to use
Sans Serif

```html
<!DOCTYPE html>
<html lang="en">
<head>
<meta charset="utf-8">
<title>BrightLoop Window Graphics</title>
<link href="https://fonts.googleapis.com/css2?family=Montserrat:ital,wght@0,500;0,600;0,700;1,800&display=swap" rel="stylesheet">
<style>
  :root{
    --backdrop:#a6a7ab;
    --blue:#2f7fd6;
    --blue-deep:#1c55b8;
    --blue-bright:#2aa4e6;
    --ink:#3a3a3d;
    --ink-deep:#2a2a2c;
    --paper:#f4f5f7;
    --white:#ffffff;
  }
  *{margin:0;padding:0;box-sizing:border-box}
  html,body{width:1200px;height:446px;overflow:hidden}
  body{background:var(--backdrop);font-family:"Montserrat",sans-serif;position:relative}
  .window-panel{position:absolute;top:74px;width:356px;height:315px;overflow:hidden;
    background:linear-gradient(125deg,var(--white) 0%,var(--paper) 30%,#e9ebee 31%,var(--paper) 45%,var(--white) 60%,#eceef1 61%,var(--paper) 100%)}
  .panel-terminal{left:29px}
  .panel-pushbutton{left:421px}
  .panel-distribution{left:813px}
  .panel-header{position:absolute;left:0;top:0;width:356px;height:48px;display:flex;align-items:center;justify-content:space-between;padding:0 16px 0 18px;color:var(--white)}
  .header-blue{background:linear-gradient(100deg,var(--blue-deep) 0%,var(--blue) 60%,var(--blue-bright) 100%)}
  .header-dark{background:var(--ink)}
  .brand-name{font-weight:500;font-size:15px;letter-spacing:.2px}
  .panel-title{font-weight:800;font-style:italic;font-size:13.5px;text-align:right;line-height:1}
  .panel-title.two-line{font-size:12.5px;line-height:13px}
  .panel-trim{position:absolute;left:0;top:0}
  .product-card{position:absolute;width:83px;height:106px}
  .product-frame{position:absolute;left:0;top:0;width:83px;height:83px;border-radius:50%;background:var(--white);
    border:3px solid var(--ink);border-top-color:var(--blue);border-left-color:var(--blue);z-index:2;padding:6px}
  .product-photo{width:100%;height:100%;border-radius:50%}
  .price-tag{position:absolute;left:6.5px;top:76px;width:70px;height:30px;border-radius:0 0 5px 5px;color:var(--white);text-align:center;padding-top:8px;z-index:1}
  .tag-dark{background:var(--ink-deep)}
  .tag-blue{background:var(--blue)}
  .sku{font-size:5.3px;font-weight:600;letter-spacing:.2px;line-height:6px}
  .price{font-size:11px;font-weight:700;line-height:12px}
  .price sup{font-size:5px;vertical-align:5px}
  .multi-price{font-size:4.3px;font-weight:600;line-height:5.4px;text-align:left;padding-left:4px;padding-top:7px}
  .multi-price sup{font-size:3px}
  .photo-grey{background:radial-gradient(circle at 50% 55%,#8d97ab 0%,#b9bfcb 45%,#eef0f3 75%)}
  .photo-yellow{background:radial-gradient(circle at 50% 55%,#2b2b2b 0%,#3a3a3a 30%,#e8b21f 55%,#f3f3f3 80%)}
  .photo-red{background:radial-gradient(circle at 50% 55%,#2b2b2b 0%,#3a3a3a 30%,#d93a2a 55%,#f3f3f3 80%)}
  .photo-block{background:radial-gradient(circle at 50% 55%,#6f7068 0%,#9a9b94 40%,#eef0f3 78%)}
  .photo-busbar{background:radial-gradient(circle at 50% 55%,#e7c51e 0%,#4e7fd4 30%,#8fb4ea 55%,#f1f4f8 80%)}
</style>
</head>
<body>

<!-- Panel: terminal enclosures -->
<section class="window-panel panel-terminal">
  <svg class="panel-trim" width="356" height="315" viewBox="0 0 356 315">
    <polygon points="0,255 55,315 0,315" fill="#2f2f31"/>
    <polygon points="15,285 265,285 290,300 40,300" fill="#1c55b8"/>
    <polygon points="40,300 290,300 300,307 50,307" fill="#2f2f31"/>
    <polygon points="300,307 356,307 356,315 306,315" fill="#1c55b8"/>
  </svg>
  <header class="panel-header header-blue"><span class="brand-name">BrightLoop</span><h2 class="panel-title">TERMINAL ENCLOSURES</h2></header>
  <div class="product-card" style="left:29.5px;top:53px"><div class="product-frame"><div class="product-photo photo-grey" role="img" aria-label="Grey terminal enclosure with open lid"></div></div><div class="price-tag tag-dark"><div class="sku">SKU: KV-AL-4P</div><div class="price">$25<sup>75</sup></div></div></div>
  <div class="product-card" style="left:136.5px;top:53px"><div class="product-frame"><div class="product-photo photo-grey" role="img" aria-label="Terminal box with terminal strip and screws"></div></div><div class="price-tag tag-blue"><div class="sku">SKU: KV-TB-20P15-GC</div><div class="price">$31<sup>20</sup></div></div></div>
  <div class="product-card" style="left:243.5px;top:53px"><div class="product-frame"><div class="product-photo photo-grey" role="img" aria-label="Light grey terminal box with screws"></div></div><div class="price-tag tag-dark"><div class="sku">SKU: KV-TB-10P15-IS</div><div class="price">$12<sup>20</sup></div></div></div>
  <div class="product-card" style="left:29.5px;top:165px"><div class="product-frame"><div class="product-photo photo-grey" role="img" aria-label="Long terminal enclosure with terminal rail"></div></div><div class="price-tag tag-blue"><div class="sku">SKU: KV-TB-20PT-IS</div><div class="price">$26<sup>00</sup></div></div></div>
  <div class="product-card" style="left:136.5px;top:165px"><div class="product-frame"><div class="product-photo photo-grey" role="img" aria-label="Terminal enclosure with 30-pole strip"></div></div><div class="price-tag tag-dark"><div class="sku">SKU: KV-TB-30P-IS</div><div class="price">$33<sup>28</sup></div></div></div>
  <div class="product-card" style="left:243.5px;top:165px"><div class="product-frame"><div class="product-photo photo-grey" role="img" aria-label="Aluminium enclosure with 12 terminals"></div></div><div class="price-tag tag-blue"><div class="sku">SKU: KV-AL-12P</div><div class="price">$41<sup>00</sup></div></div></div>
</section>

<!-- Panel: push button enclosures -->
<section class="window-panel panel-pushbutton">
  <svg class="panel-trim" width="356" height="315" viewBox="0 0 356 315">
    <polygon points="356,245 356,315 300,315" fill="#1c55b8"/>
    <polygon points="90,285 340,285 315,300 70,300" fill="#2f2f31"/>
    <polygon points="50,300 315,300 305,307 40,307" fill="#1c55b8"/>
    <polygon points="0,307 40,307 34,315 0,315" fill="#2f2f31"/>
  </svg>
  <header class="panel-header header-dark"><span class="brand-name">BrightLoop</span><h2 class="panel-title">PUSH BUTTON ENCLOSURES</h2></header>
  <div class="product-card" style="left:29.5px;top:53px"><div class="product-frame"><div class="product-photo photo-yellow" role="img" aria-label="Yellow one-hole push button box"></div></div><div class="price-tag tag-dark"><div class="sku">SKU: KV-PB-2501Y</div><div class="price">$13<sup>62</sup></div></div></div>
  <div class="product-card" style="left:136.5px;top:53px"><div class="product-frame"><div class="product-photo photo-yellow" role="img" aria-label="Yellow two-hole push button box"></div></div><div class="price-tag tag-blue"><div class="sku">SKU: KV-PB-2502Y</div><div class="price">$18<sup>02</sup></div></div></div>
  <div class="product-card" style="left:243.5px;top:53px"><div class="product-frame"><div class="product-photo photo-red" role="img" aria-label="Red one-hole push button box"></div></div><div class="price-tag tag-dark"><div class="sku">SKU: KV-PB-2501R</div><div class="price">$13<sup>62</sup></div></div></div>
  <div class="product-card" style="left:29.5px;top:165px"><div class="product-frame"><div class="product-photo photo-red" role="img" aria-label="Red two-hole push button box"></div></div><div class="price-tag tag-blue"><div class="sku">SKU: KV-PB-2502R</div><div class="price">$18<sup>02</sup></div></div></div>
  <div class="product-card" style="left:136.5px;top:165px"><div class="product-frame"><div class="product-photo photo-yellow" role="img" aria-label="Yellow three-hole push button box"></div></div><div class="price-tag tag-dark"><div class="sku">SKU: KV-PB-2203Y</div><div class="price">$22<sup>00</sup></div></div></div>
  <div class="product-card" style="left:243.5px;top:165px"><div class="product-frame"><div class="product-photo photo-yellow" role="img" aria-label="Yellow four-hole push button box"></div></div><div class="price-tag tag-blue"><div class="sku">SKU: KV-PB-2204Y</div><div class="price">$26<sup>00</sup></div></div></div>
</section>

<!-- Panel: DIN rail power distribution blocks -->
<section class="window-panel panel-distribution">
  <svg class="panel-trim" width="356" height="315" viewBox="0 0 356 315">
    <polygon points="0,255 55,315 0,315" fill="#2f2f31"/>
    <polygon points="15,285 265,285 290,300 40,300" fill="#1c55b8"/>
    <polygon points="40,300 290,300 300,307 50,307" fill="#2f2f31"/>
    <polygon points="300,307 356,307 356,315 306,315" fill="#1c55b8"/>
  </svg>
  <header class="panel-header header-blue"><span class="brand-name">BrightLoop</span><h2 class="panel-title two-line">DIN RAIL MOUNTABLE POWER<br>DISTRIBUTION BLOCKS</h2></header>
  <div class="product-card" style="left:29.5px;top:53px"><div class="product-frame"><div class="product-photo photo-block" role="img" aria-label="Grey 4-pole distribution block"></div></div><div class="price-tag tag-dark"><div class="sku">SKU: KV-PD-100-4P</div><div class="price">$18<sup>50</sup></div></div></div>
  <div class="product-card" style="left:136.5px;top:53px"><div class="product-frame"><div class="product-photo photo-block" role="img" aria-label="Grey 6-pole distribution block"></div></div><div class="price-tag tag-blue"><div class="sku">SKU: KV-PD-100-6P</div><div class="price">$19<sup>85</sup></div></div></div>
  <div class="product-card" style="left:243.5px;top:53px"><div class="product-frame"><div class="product-photo photo-block" role="img" aria-label="Three grey distribution blocks in a row"></div></div><div class="price-tag tag-dark multi-price"><div>SKU: KV-PD-200-4P &nbsp;$22<sup>20</sup></div><div>SKU: KV-PD-200-6P &nbsp;$23<sup>40</sup></div><div>SKU: KV-PD-200-8P &nbsp;$26<sup>10</sup></div></div></div>
  <div class="product-card" style="left:29.5px;top:165px"><div class="product-frame"><div class="product-photo photo-busbar" role="img" aria-label="Blue 3-level busbar block"></div></div><div class="price-tag tag-blue"><div class="sku">SKU: KV-PD3L10-100A</div><div class="price">$33<sup>00</sup></div></div></div>
  <div class="product-card" style="left:136.5px;top:165px"><div class="product-frame"><div class="product-photo photo-busbar" role="img" aria-label="Blue 3-level 200A busbar block"></div></div><div class="price-tag tag-dark"><div class="sku">SKU: KV-PD3L10-200A</div><div class="price">$49<sup>50</sup></div></div></div>
  <div class="product-card" style="left:243.5px;top:165px"><div class="product-frame"><div class="product-photo photo-busbar" role="img" aria-label="Blue 4-level busbar block"></div></div><div class="price-tag tag-blue"><div class="sku">SKU: KV-PD4L10-100A</div><div class="price">$46<sup>85</sup></div></div></div>
</section>

</body>
</html>
```